E-commerce Website - new look and feel

Link to website
http://198.51.100.64/~vorpanet/vorpanetix_ecommerce/index.php#

Home page
-Header
- -Search bar and add to cart
-Drop down - Multi layer category representation: 1st main category level in menu bar style, 2nd category to follow and 3rd category
-Banner
-Footer

-Search listing

Category page
-Product listing
-

Product detail page
-Product variation tabular view
-

Checkout page
-

404 link/product image not found
Should be fun and engaging customers

Recent search products/ preferred products for customers

all pages:
Headroom js search bar once you are lower down the page

Shrinking navbar

Target Market(s)

Telecommunication installers, electricians working on Industrial plants and projects, on the move customers that need immediate products, procurement officers buying for projects, hard to get items customers, Car hobbyists ( future market ) for some specific product like stainless steel braid(sleeve)

Industry/Entity Type

Telecommunications

Number of Pages Required

5+ page

Colors

Designer to choose colors to be used in the design.

Requirements
Must have
• - less cluttered design
• - Easy to navigate
• - more white area on all pages
• - quick orders
• - repetitive product ordering by customers menu/list
• - branding consistency, logo colours and design
Nice to have
• -modern look
• -user friendly for less technical and computer skilled customers
• -quick to navigate
• - fun text to make customer feel at ease when navigating through website
Should not have
• -too much details
• -

```html
<!DOCTYPE html>
<html lang="en">
<head>
<meta charset="utf-8">
<title>Vorpanetix — Harbour Components Store</title>
<link rel="stylesheet" href="https://fonts.googleapis.com/css2?family=Poppins:wght@400;500;600;700&family=Montserrat:wght@400;500;600;700&display=swap">
<style>
:root{
  --brand:#0f6fb8;
  --brand-dark:#0b4f8f;
  --ink:#3d4a57;
  --ink-soft:#6b7580;
  --muted:#9aa3ad;
  --page:#f4f6f9;
  --card:#ffffff;
  --line:#e6eaef;
}
*{box-sizing:border-box;margin:0;padding:0}
html,body{width:1200px;height:2233px;overflow:hidden}
body{position:relative;background:var(--page);font-family:"Montserrat",sans-serif;color:var(--ink)}
.abs{position:absolute}

/* top bar */
.topbar{left:0;top:0;width:1200px;height:47px;background:#fff;border-bottom:1px solid var(--line)}
.contact-list{left:144px;top:16px;display:flex;gap:22px;align-items:center}
.contact-item{font-size:10.5px;color:var(--ink-soft);display:flex;align-items:center;gap:7px;white-space:nowrap;line-height:12px}
.social{top:19px;display:flex;gap:14px;left:978px}
.social span{width:9px;height:9px;border-radius:50%;background:var(--ink)}

/* header */
.header{left:0;top:47px;width:1200px;height:94px;background:#fff}
.logo{left:150px;top:60px;width:104px;text-align:center}
.logo-mark{width:22px;height:22px;border-radius:50%;background:var(--brand);margin:0 auto 6px}
.logo-name{font-family:"Poppins",sans-serif;font-weight:700;font-size:12px;color:var(--ink);letter-spacing:.5px;line-height:1}
.logo-sub{font-size:6px;color:var(--ink-soft);letter-spacing:.8px;margin-top:2px;white-space:nowrap}
.nav{top:90px;left:322px;font-size:12px;font-weight:500;color:var(--ink)}
.nav a{color:inherit;text-decoration:none;position:absolute;white-space:nowrap;top:0}
.nav a.active{color:var(--brand)}
.header-icon{top:88px}
.cart-badge{left:1038px;top:77px;width:13px;height:13px;border-radius:50%;background:var(--ink);color:#fff;font-size:8px;text-align:center;line-height:13px}

/* hero */
.hero{left:0;top:141px;width:1200px;height:506px;background:radial-gradient(ellipse at 72% 30%,#5fb4ff 0%,#1d6fd6 30%,#0c3f9a 65%,#082c70 100%)}
.hero-title{left:217px;top:322px;font-family:"Poppins",sans-serif;font-weight:700;font-size:27px;color:#fff;letter-spacing:.3px;white-space:nowrap}
.hero-text{left:217px;top:376px;width:560px;font-size:12.5px;line-height:19px;color:#e8f1ff}
.hero-meta{left:217px;top:451px;display:flex;gap:26px;font-size:13px;color:#fff;align-items:center}
.hero-meta .order{display:flex;gap:8px;align-items:center}
.slider-dots{left:144px;top:360px;width:7px}
.slider-dots span{display:block;width:7px;height:14px;background:#fff;margin-bottom:20px}
.slider-dots span.on{background:#2e8cf0;height:20px}

/* section heads */
.section-head{left:0;width:1200px;text-align:center}
.section-head h2{font-family:"Poppins",sans-serif;font-weight:700;font-size:27px;color:var(--ink);letter-spacing:.3px}
.section-head h2 b{color:var(--brand);font-weight:700}
.section-head p{margin-top:14px;font-size:12px;color:var(--ink-soft)}

/* product cards */
.product-card{top:860px;width:210px;height:284px;background:var(--card);text-align:center}
.product-card.raised{box-shadow:0 6px 18px rgba(30,50,80,.14)}
.product-photo{position:absolute;left:25px;top:30px;width:160px;height:110px;border-radius:4px}
.product-name{position:absolute;left:0;right:0;top:217px;font-size:13px;font-weight:700;color:var(--ink)}
.product-price{position:absolute;left:0;right:0;top:246px;font-size:13px;font-weight:700;color:var(--brand)}
.raised .product-name{top:176px;font-size:12px}
.sizes{position:absolute;left:0;right:0;top:205px;font-size:10px;color:var(--ink-soft)}
.card-actions{position:absolute;left:0;right:0;top:240px;display:flex;justify-content:center;gap:28px}

.pager{left:144px;top:1208px;width:912px;height:45px;background:#fff;display:flex;justify-content:center;align-items:center;gap:5px}
.pager span{width:6px;height:6px;border-radius:50%;background:var(--brand)}

/* category tiles */
.category-tile{top:1315px;height:206px;display:flex;align-items:center;justify-content:center;text-align:center;font-family:"Poppins",sans-serif;font-weight:600;font-size:19px;line-height:24px;color:#fff}

/* best sales */
.sale-card{top:1720px;width:289px;height:124px;background:#fff}
.sale-card.raised{box-shadow:0 6px 18px rgba(30,50,80,.14)}
.sale-photo{position:absolute;left:22px;top:30px;width:80px;height:62px;border-radius:4px}
.sale-divider{position:absolute;left:120px;top:40px;width:1px;height:44px;background:var(--line)}
.sale-name{position:absolute;left:134px;top:37px;font-size:13px;font-weight:700;color:var(--ink);white-space:nowrap}
.sale-row{position:absolute;left:134px;top:68px;display:flex;align-items:center;gap:8px;font-size:12px;font-weight:600;color:var(--brand);white-space:nowrap}
.sale-row .price{margin-left:12px}

/* newsletter */
.newsletter{left:144px;top:1914px;width:912px;height:96px;background:#fff}
.nl-title{position:absolute;left:43px;top:40px;font-size:12px;font-weight:700;color:var(--brand-dark)}
.nl-text{position:absolute;left:148px;top:41px;font-size:10px;font-style:italic;color:var(--ink)}
.nl-field{position:absolute;left:555px;top:40px;display:flex;gap:8px;align-items:center;font-size:10px;font-style:italic;color:var(--muted)}
.nl-button{position:absolute;left:801px;top:29px;width:78px;height:38px;background:var(--brand);color:#fff;font-size:11px;font-weight:600;text-align:center;line-height:38px}

/* footer */
.footer{left:0;top:2043px;width:1200px;height:190px;background:#fff}
.copyright{left:144px;top:2156px;font-size:11px;color:var(--ink)}
.footer-col{list-style:none;font-size:11px;color:var(--ink);line-height:23.5px;top:2104px}
.footer-col li::before{content:"• ";color:var(--ink)}
.footer-col li.link{color:var(--brand)}
.pay-title{left:922px;top:2116px;font-size:12px;font-weight:700;color:var(--brand)}
.pay-cards{left:922px;top:2144px;display:flex;gap:6px}
.pay-cards span{width:19px;height:13px;border-radius:2px}
</style>
</head>
<body>

<div class="abs topbar"></div>
<div class="abs contact-list">
  <div class="contact-item">
    <svg width="14" height="10" viewBox="0 0 14 10"><rect x=".5" y=".5" width="13" height="9" fill="none" stroke="#0f6fb8"/><path d="M.5 .5 7 6l6.5-5.5" fill="none" stroke="#0f6fb8"/></svg>
    sales@harbourcomponents.example
  </div>
  <div class="contact-item">
    <svg width="9" height="11" viewBox="0 0 9 11"><rect x=".5" y=".5" width="8" height="10" rx="1" fill="none" stroke="#0f6fb8"/><rect x="2" y="2" width="5" height="6" fill="#0f6fb8"/></svg>
    1300 555 014
  </div>
</div>
<div class="abs social" aria-label="Social links"><span></span><span></span><span></span><span></span></div>

<header class="abs header"></header>
<div class="abs logo">
  <div class="logo-mark"></div>
  <div class="logo-name">VORPANETIX</div>
  <div class="logo-sub">ASIA PACIFIC PTY LTD</div>
</div>
<nav class="abs nav">
  <a class="active" href="http://198.51.100.64/~vorpanet/vorpanetix_ecommerce/index.php#" style="left:0">Home</a>
  <a href="#" style="left:59px">Products</a>
  <a href="#" style="left:134px">Hot Deals</a>
  <a href="#" style="left:218px">About</a>
  <a href="#" style="left:280px">Contact</a>
</nav>
<svg class="abs header-icon" style="left:956px" width="15" height="15" viewBox="0 0 15 15"><circle cx="6" cy="6" r="5" fill="none" stroke="#3d4a57" stroke-width="1.4"/><path d="M10 10l4 4" stroke="#3d4a57" stroke-width="1.4"/></svg>
<svg class="abs header-icon" style="left:998px" width="16" height="15" viewBox="0 0 16 15"><circle cx="8" cy="5" r="4" fill="none" stroke="#3d4a57" stroke-width="1.3"/><path d="M1 14c1-4 4-5 7-5s6 1 7 5z" fill="none" stroke="#3d4a57" stroke-width="1.3"/></svg>
<svg class="abs header-icon" style="left:1037px" width="17" height="15" viewBox="0 0 17 15"><path d="M1 5h15l-2 9H3z" fill="none" stroke="#0f6fb8" stroke-width="1.4"/><path d="M5 5l3-4 3 4" fill="none" stroke="#0f6fb8" stroke-width="1.4"/></svg>
<div class="abs cart-badge">0</div>

<section class="abs hero" role="img" aria-label="Close-up of blue network patch cables with glowing fibre optic strands"></section>
<div class="abs slider-dots"><span></span><span class="on"></span><span></span></div>
<h1 class="abs hero-title">HARBOUR COMPONENTS PRODUCTS</h1>
<p class="abs hero-text">Free Freight On Orders Over $150 Excluding GST (VIC, NSW, QLD, SA) Free Freight On Orders Over $250 Excluding GST (WA, NT)</p>
<div class="abs hero-meta">
  <span>Price : $120</span>
  <span class="order"><svg width="17" height="13" viewBox="0 0 17 13"><path d="M1 4h15l-2 8H3z" fill="none" stroke="#fff" stroke-width="1.3"/><path d="M5 4l3-3 3 3" fill="none" stroke="#fff" stroke-width="1.3"/></svg>Order Now</span>
</div>

<div class="abs section-head" style="top:733px">
  <h2><b>NEW</b> ARRIVALS</h2>
  <p>Lorem Ipsum is simply dummy text of the printing and typesetting industry</p>
</div>

<div class="abs product-card" style="left:144px">
  <div class="product-photo" role="img" aria-label="Rainbow jumper wire leads" style="background:linear-gradient(135deg,#f6f7f9,#dfe6ee 50%,#f6f7f9)"></div>
  <div class="product-name">Lorem Ipsum</div>
  <div class="product-price">100$</div>
</div>
<div class="abs product-card" style="left:378px">
  <div class="product-photo" role="img" aria-label="Blue network cable with clear RJ45 plug" style="background:linear-gradient(135deg,#ffffff,#cfe6fa 55%,#ffffff)"></div>
  <div class="product-name" style="top:213px">Lorem Ipsum</div>
  <div class="product-price">100$</div>
</div>
<div class="abs product-card raised" style="left:612px">
  <div class="product-photo" role="img" aria-label="Coil of green and yellow earth wire" style="background:radial-gradient(ellipse,#fff 25%,#c9dc55 45%,#9fbf2e 60%,#fff 72%)"></div>
  <div class="product-name">CAP RB25</div>
  <div class="sizes">sizes &nbsp; : &nbsp; s - m - l - xl</div>
  <div class="card-actions">
    <svg width="14" height="14" viewBox="0 0 14 14"><circle cx="7" cy="7" r="6" fill="none" stroke="#3d4a57" stroke-width="1.2"/><path d="M1 7h12M7 1c3 3 3 9 0 12M7 1c-3 3-3 9 0 12" fill="none" stroke="#3d4a57" stroke-width="1"/></svg>
    <svg width="17" height="14" viewBox="0 0 17 14"><path d="M1 1h3l2 8h8l2-6H6" fill="none" stroke="#0f6fb8" stroke-width="1.3"/><circle cx="7" cy="12" r="1.2" fill="#0f6fb8"/><circle cx="13" cy="12" r="1.2" fill="#0f6fb8"/></svg>
    <svg width="15" height="13" viewBox="0 0 15 13"><path d="M7.5 12S1 8 1 4.2A3.2 3.2 0 0 1 7.5 3a3.2 3.2 0 0 1 6.5 1.2C14 8 7.5 12 7.5 12z" fill="none" stroke="#3d4a57" stroke-width="1.2"/></svg>
  </div>
</div>
<div class="abs product-card" style="left:846px">
  <div class="product-photo" role="img" aria-label="Cross-section of a multicore cable" style="background:radial-gradient(ellipse at 40% 50%,#c9743a 0%,#6a6a6a 40%,#2c2c2c 65%,#fff 80%)"></div>
  <div class="product-name" style="top:213px">Lorem Ipsum</div>
  <div class="product-price">100$</div>
</div>

<div class="abs pager"><span></span><span></span><span></span></div>

<div class="abs category-tile" style="left:144px;width:521px;background:linear-gradient(135deg,#3f6d92,#2e5a80 50%,#4a7598)" role="img" aria-label="Metal earthing fittings and screws">Telecommunications Earthing<br>Accessories</div>
<div class="abs category-tile" style="left:691px;width:365px;background:linear-gradient(135deg,#6d6e72,#5d5e62 50%,#77787c)" role="img" aria-label="Coloured tapes, rope and cable ties">General<br>Consumables</div>

<div class="abs section-head" style="top:1595px">
  <h2><b>BEST</b> SALES</h2>
  <p>Lorem Ipsum is simply dummy text of the printing and typesetting industry</p>
</div>

<div class="abs sale-card" style="left:144px">
  <div class="sale-photo" role="img" aria-label="Red cable connector" style="background:radial-gradient(ellipse,#e23a3a 20%,#fbe3e3 50%,#fff 70%)"></div>
  <div class="sale-divider"></div>
  <div class="sale-name">Trail Track Jacket</div>
  <div class="sale-row"><svg width="17" height="14" viewBox="0 0 17 14"><path d="M1 1h3l2 8h8l2-6H6" fill="none" stroke="#0f6fb8" stroke-width="1.3"/><circle cx="7" cy="12" r="1.2" fill="#0f6fb8"/><circle cx="13" cy="12" r="1.2" fill="#0f6fb8"/></svg>add to cart<span class="price">100$</span></div>
</div>
<div class="abs sale-card raised" style="left:456px">
  <div class="sale-photo" role="img" aria-label="Black cable gland fitting" style="background:radial-gradient(ellipse,#222 18%,#d8d8d8 45%,#fff 68%)"></div>
  <div class="sale-divider"></div>
  <div class="sale-name">Trail Track Jacket</div>
  <div class="sale-row"><svg width="17" height="14" viewBox="0 0 17 14"><path d="M1 1h3l2 8h8l2-6H6" fill="none" stroke="#0f6fb8" stroke-width="1.3"/><circle cx="7" cy="12" r="1.2" fill="#0f6fb8"/><circle cx="13" cy="12" r="1.2" fill="#0f6fb8"/></svg>add to cart<span class="price">100$</span></div>
</div>
<div class="abs sale-card" style="left:767px">
  <div class="sale-photo" role="img" aria-label="Orange extension lead" style="background:radial-gradient(ellipse,#f05a22 25%,#fde2d6 52%,#fff 70%)"></div>
  <div class="sale-divider"></div>
  <div class="sale-name">Trail Track Jacket</div>
  <div class="sale-row"><svg width="17" height="14" viewBox="0 0 17 14"><path d="M1 1h3l2 8h8l2-6H6" fill="none" stroke="#0f6fb8" stroke-width="1.3"/><circle cx="7" cy="12" r="1.2" fill="#0f6fb8"/><circle cx="13" cy="12" r="1.2" fill="#0f6fb8"/></svg>add to cart<span class="price">100$</span></div>
</div>

<div class="abs newsletter">
  <div class="nl-title">NEWS LETTER</div>
  <div class="nl-text">join us now to get all news and special offers</div>
  <div class="nl-field"><svg width="14" height="10" viewBox="0 0 14 10"><rect x=".5" y=".5" width="13" height="9" fill="none" stroke="#0f6fb8"/><path d="M.5 .5 7 6l6.5-5.5" fill="none" stroke="#0f6fb8"/></svg>type your email here</div>
  <div class="nl-button">join us</div>
</div>

<footer class="abs footer"></footer>
<div class="abs logo" style="left:162px;top:2078px">
  <div class="logo-mark"></div>
  <div class="logo-name">VORPANETIX</div>
  <div class="logo-sub">ASIA PACIFIC PTY LTD</div>
</div>
<div class="abs copyright">shopy c 2018 . your copy right here</div>
<ul class="abs footer-col" style="left:456px"><li class="link">about us</li><li>contact us</li><li>support</li></ul>
<ul class="abs footer-col" style="left:615px"><li>our feed</li><li>terms and conditions</li><li>our privacy</li></ul>
<ul class="abs footer-col" style="left:767px"><li>join us</li><li>live support</li></ul>
<div class="abs pay-title">Payment Methods</div>
<div class="abs pay-cards" aria-label="Accepted payment methods">
  <span style="background:#5aa7e0"></span><span style="background:#f0a64a"></span><span style="background:#e25555"></span><span style="background:#7b6fd0"></span><span style="background:#c9cdd2"></span>
</div>

</body>
</html>
```